Brindmoor Gardening Fresh New Website

We are looking to create a simple fresh website for our landscaping business. The website should appeal to a 'high end' audience. We deal with a lot of Embassies and affluent clients who have extremely large gardens that are meticulously maintained. The site is about communicating our excellent landscaping and customer service skills and encouraging new clients to reach out and engage us to take care of their gardens.

The website is basically going to be our business card, it will have almost no functionality other than two 'contact us' forms, one for smaller clients and one for more detailed projects.

The website will not have a lot of written content and will have to show photos of beautifully landscaped gardens.

The main logo in black will influence the site, however, we are open to all suggestions.

We are expecting to have the following pages:
Home Page
Services
About Us
Contact Us
Showcase (photo gallery of our work)

We need someone who can code it to wordpress and be available for minor changes over a number of days. They will be simple tweaks.

```html
<!DOCTYPE html>
<html lang="en">
<head>
<meta charset="utf-8">
<title>Brindmoor Gardening</title>
<link rel="stylesheet" href="https://fonts.googleapis.com/css2?family=Noto+Serif:wght@400;500;700&display=swap">
<style>
:root{
  --gold-dark:#b5852a;
  --gold:#d9ad3c;
  --gold-light:#f3cf4f;
  --ink:#1b1b1b;
  --text:#3a3a3a;
  --muted:#8a8a8a;
  --panel:#f3f3f3;
  --white:#ffffff;
  --footer:#1d1d1d;
  --field:#ffffff;
}
*{margin:0;padding:0;box-sizing:border-box}
html,body{width:1200px;height:4342px;overflow:hidden}
body{position:relative;background:var(--white);font-family:"Noto Serif",Georgia,serif;color:var(--ink)}
.abs{position:absolute}
.gold-btn{position:absolute;display:flex;align-items:center;justify-content:center;background:linear-gradient(90deg,var(--gold-dark),var(--gold-light) 55%,var(--gold-dark));color:#2a2110;font-size:14px;font-weight:500;letter-spacing:.3px;border-radius:6px;box-shadow:0 2px 6px rgba(0,0,0,.18)}
.section-title{position:absolute;left:0;width:1200px;text-align:center;font-size:34px;font-weight:500;letter-spacing:.5px;color:var(--ink)}

/* hero */
.hero-photo{left:0;top:0;width:1200px;height:700px;background:
  radial-gradient(ellipse 260px 200px at 700px 260px,rgba(235,235,225,.55),transparent 70%),
  radial-gradient(ellipse 140px 120px at 700px 450px,rgba(200,90,40,.55),transparent 70%),
  radial-gradient(ellipse 330px 420px at 960px 330px,#1f6650 0%,#174c3d 55%,transparent 80%),
  radial-gradient(ellipse 380px 520px at 160px 330px,#4e7a2c 0%,#355a1d 45%,transparent 80%),
  radial-gradient(ellipse 300px 160px at 420px 500px,rgba(70,70,55,.7),transparent 75%),
  radial-gradient(ellipse 240px 200px at 560px 120px,#5b8a38,transparent 75%),
  linear-gradient(110deg,#2c4a1a 0%,#3f6226 35%,#2f5232 62%,#1c4234 100%)}
.hero-shade{left:0;top:0;width:1200px;height:700px;background:linear-gradient(180deg,rgba(0,0,0,.28),rgba(0,0,0,.05) 40%,rgba(0,0,0,.18))}
.topbar{color:var(--white);font-size:14px}
.nav-link{color:var(--white);font-size:14px;letter-spacing:.3px}
.nav-rule{height:1px;background:rgba(255,255,255,.45)}
.brand{left:450px;width:300px;text-align:center;color:var(--white);font-weight:400}
.brand-name{font-size:21px;letter-spacing:9px}
.brand-sub{font-size:12px;letter-spacing:7px;margin-top:6px}
.hero-title{left:0;top:222px;width:1200px;text-align:center;color:var(--white);font-size:42px;font-weight:500;letter-spacing:4px;line-height:51px;text-shadow:0 2px 8px rgba(0,0,0,.3)}

/* about */
.about-photo-ring{left:151px;top:695px;width:372px;height:372px;border-radius:50%;border:2px solid var(--gold-light)}
.about-photo{left:163px;top:707px;width:348px;height:348px;border-radius:50%;background:
  radial-gradient(ellipse 90px 60px at 100px 150px,#8cc04a,transparent 75%),
  radial-gradient(ellipse 70px 50px at 220px 150px,#a9855a,transparent 75%),
  radial-gradient(ellipse 80px 70px at 250px 240px,#d9a98a,transparent 75%),
  radial-gradient(ellipse 90px 60px at 130px 250px,#7db548,transparent 75%),
  radial-gradient(ellipse 120px 80px at 200px 60px,#8a8a82,transparent 75%),
  linear-gradient(180deg,#6f6a5e 0%,#5a6a3c 35%,#3e2f22 70%,#2a1e14 100%)}
.about-title{left:558px;top:718px;font-size:35px;font-weight:500;line-height:40px;letter-spacing:.5px}
.about-copy{left:558px;top:820px;width:472px;font-size:16px;line-height:26.6px;color:var(--text)}

/* services */
.card{position:absolute;top:1306px;width:294px;height:362px;background:var(--white);box-shadow:0 4px 14px rgba(0,0,0,.12)}
.card-img{width:294px;height:214px}
.card-name{position:absolute;left:25px;top:234px;font-size:19px;font-weight:700}
.card-desc{position:absolute;left:25px;top:270px;width:200px;font-size:13.5px;line-height:18px;color:var(--muted)}
.card-arrow{position:absolute;left:236px;top:308px}

/* why */
.why-item{position:absolute;top:2040px;width:210px;text-align:center}
.why-ring{margin:0 auto;width:142px;height:142px;border-radius:50%;border:3px solid var(--gold);display:flex;align-items:center;justify-content:center;background:var(--white)}
.why-icon{width:96px;height:96px;border-radius:50%;border:1.5px solid var(--gold);background:radial-gradient(circle at 50% 45%,#fdf6e2 0%,#f6e3ab 55%,#e9c86a 100%)}
.why-text{margin-top:28px;font-size:19px;font-weight:700;line-height:25px}

/* gallery */
.tile{position:absolute}

/* contact */
.contact-bg{left:0;top:3220px;width:1200px;height:740px;background:
  radial-gradient(ellipse 300px 260px at 1080px 220px,#e2e4de,transparent 75%),
  radial-gradient(ellipse 400px 200px at 200px 560px,#e6e7e2,transparent 75%),
  #efefed}
.field{position:absolute;background:var(--field);border-radius:6px;font-size:13px;color:#333;padding:14px 12px}

/* footer */
.footer{left:0;top:3930px;width:1200px;height:412px;background:var(--footer)}
.f-head{position:absolute;top:3982px;color:var(--white);font-size:21px;font-weight:500;letter-spacing:.5px}
.f-rule{position:absolute;top:4030px;width:66px;height:1px;background:#cfcfcf}
.f-list{position:absolute;top:4054px;color:#e6e6e6;font-size:14px;line-height:23px;list-style:none}
.f-contact{position:absolute;left:818px;color:#e6e6e6;font-size:14px;line-height:18px;display:flex;gap:9px}
.f-brand{left:473px;top:4082px;width:300px;text-align:center;color:var(--gold)}
.f-brand .brand-name{font-size:30px;letter-spacing:11px}
.f-brand .brand-sub{font-size:16px;letter-spacing:10px;margin-top:8px}
.f-divider{left:115px;top:4218px;width:943px;height:1px;background:#3a3a3a}
.copyright{left:0;top:4247px;width:1200px;text-align:center;color:var(--white);font-size:14px}
</style>
</head>
<body>

<!-- hero -->
<div class="abs hero-photo" role="img" aria-label="Gardener trimming a tall green hedge with hedge shears"></div>
<div class="abs hero-shade"></div>
<div class="abs topbar" style="left:229px;top:35px">CALL: 212 555 0184</div>
<div class="abs nav-link" style="left:826px;top:35px;color:var(--gold-light)">REQUEST A QUOTE</div>
<div class="abs nav-rule" style="left:229px;top:79px;width:310px"></div>
<div class="abs nav-rule" style="left:650px;top:79px;width:322px"></div>
<div class="abs nav-link" style="left:229px;top:108px">SERVICES</div>
<div class="abs nav-link" style="left:350px;top:108px">ABOUT US</div>
<div class="abs nav-link" style="left:745px;top:108px">CONTACT US</div>
<div class="abs nav-link" style="left:885px;top:108px">SHOWCASE</div>
<div class="abs brand" style="top:96px"><div class="brand-name">BRINDMOOR</div><div class="brand-sub">GARDENING</div></div>
<h1 class="abs hero-title">WELCOME TO<br>BRINDMOOR GARDENING</h1>
<div class="gold-btn" style="left:502px;top:356px;width:196px;height:48px">REQUEST A QUOTE</div>

<!-- about band -->
<svg class="abs" style="left:0;top:580px" width="1200" height="620" viewBox="0 580 1200 620">
  <defs>
    <linearGradient id="goldGrad" x1="0" x2="1"><stop offset="0" stop-color="#b5852a"/><stop offset=".5" stop-color="#f3cf4f"/><stop offset="1" stop-color="#c99a30"/></linearGradient>
  </defs>
  <path d="M0 670 Q600 540 1200 670 L1200 1095 Q600 1230 0 1095 Z" fill="#f3f3f3"/>
  <path d="M140 640 Q600 560 1060 640 Q600 578 140 640 Z" fill="url(#goldGrad)"/>
  <path d="M60 1110 Q600 1205 1080 1112 Q600 1180 60 1110 Z" fill="url(#goldGrad)"/>
</svg>
<div class="abs about-photo-ring"></div>
<div class="abs about-photo" role="img" aria-label="Hands planting lettuce seedlings in dark soil with garden tools behind"></div>
<h2 class="abs about-title">ABOUT<br>BRINDMOOR GARDENING</h2>
<p class="abs about-copy">Lorem ipsum dolor sit amet, consectetur adipiscing elit, sed do eiusmod tempor incididunt ut labore et dolore magna aliqua. Quis ipsum suspendisse ultrices gravida. Risus commodo viverra maecenas accumsan lacus vel facilisis. Lorem ipsum dolor sit amet, consectetur adi piscing elit, sed do eiusmod tempor incididunt ut lab ore et dolore magna aliqua. Quis ipsum suspendisse ultrices gravida.</p>

<!-- services -->
<h2 class="section-title" style="top:1230px">OUR SERVICES</h2>
<div class="card" style="left:126px">
  <div class="card-img" role="img" aria-label="Gloved hands trimming a green shrub with electric hedge trimmer" style="background:
    radial-gradient(ellipse 70px 50px at 220px 80px,#d8dcd2,transparent 75%),
    radial-gradient(ellipse 60px 40px at 200px 140px,#2f8a3a,transparent 75%),
    radial-gradient(ellipse 120px 90px at 80px 120px,#8fbf3a,transparent 75%),
    radial-gradient(ellipse 140px 80px at 120px 200px,#4f7e1e,transparent 80%),
    linear-gradient(135deg,#4a7a20,#6e9e2a 50%,#2f4e14)"></div>
  <div class="card-name">Service Name1</div>
  <div class="card-desc">Lorem ipsum dolor sitm onsectetur adipiscin.</div>
  <svg class="card-arrow" width="44" height="26" viewBox="0 0 44 26" fill="none" stroke="#d9ad3c" stroke-width="2"><path d="M2 13 L14 2 L26 13 L14 24 Z"/><path d="M16 13 H40 M33 6 L40 13 L33 20"/></svg>
</div>
<div class="card" style="left:453px">
  <div class="card-img" role="img" aria-label="Green lawn mower on a freshly cut lawn" style="background:
    radial-gradient(ellipse 80px 60px at 110px 120px,#2e6a36,transparent 75%),
    radial-gradient(ellipse 90px 40px at 110px 70px,#3a3a3a,transparent 75%),
    radial-gradient(ellipse 120px 50px at 240px 40px,#eef0ea,transparent 75%),
    linear-gradient(180deg,#cfd8c2 0%,#9ab86a 35%,#5f9a2c 60%,#4a8a22 100%)"></div>
  <div class="card-name">Service Name 2</div>
  <div class="card-desc">Lorem ipsum dolor sitm onsectetur adipiscin.</div>
  <svg class="card-arrow" width="44" height="26" viewBox="0 0 44 26" fill="none" stroke="#d9ad3c" stroke-width="2"><path d="M2 13 L14 2 L26 13 L14 24 Z"/><path d="M16 13 H40 M33 6 L40 13 L33 20"/></svg>
</div>
<div class="card" style="left:777px">
  <div class="card-img" role="img" aria-label="Gardener in orange uniform planting a flower bed" style="background:
    radial-gradient(ellipse 50px 60px at 190px 80px,#e8742a,transparent 75%),
    radial-gradient(ellipse 50px 40px at 215px 135px,#4e8a2e,transparent 75%),
    radial-gradient(ellipse 110px 50px at 110px 180px,#a4506a,transparent 80%),
    radial-gradient(ellipse 120px 80px at 60px 70px,#7aa03a,transparent 75%),
    linear-gradient(160deg,#5f8a34,#8aac4a 50%,#4a6a28)"></div>
  <div class="card-name">Service Name 3</div>
  <div class="card-desc">Lorem ipsum dolor sitm onsectetur adipiscin.</div>
  <svg class="card-arrow" width="44" height="26" viewBox="0 0 44 26" fill="none" stroke="#d9ad3c" stroke-width="2"><path d="M2 13 L14 2 L26 13 L14 24 Z"/><path d="M16 13 H40 M33 6 L40 13 L33 20"/></svg>
</div>
<div class="gold-btn" style="left:500px;top:1707px;width:198px;height:50px">VIEW ALL SERVICES</div>

<!-- why different band -->
<svg class="abs" style="left:0;top:1840px" width="1200" height="560" viewBox="0 1840 1200 560">
  <defs>
    <linearGradient id="goldGrad2" x1="0" x2="1"><stop offset="0" stop-color="#b5852a"/><stop offset=".5" stop-color="#f3cf4f"/><stop offset="1" stop-color="#c99a30"/></linearGradient>
  </defs>
  <path d="M0 1915 Q600 1810 1200 1915 L1200 2308 Q600 2450 0 2308 Z" fill="#f3f3f3"/>
  <path d="M135 1900 Q600 1830 1065 1900 Q600 1848 135 1900 Z" fill="url(#goldGrad2)"/>
  <path d="M80 2330 Q600 2425 1100 2332 Q600 2398 80 2330 Z" fill="url(#goldGrad2)"/>
</svg>
<h2 class="section-title" style="top:1955px">WHY WE’RE DIFFERENT</h2>
<div class="why-item" style="left:79px"><div class="why-ring"><div class="why-icon" role="img" aria-label="Trowel and potted seedling icon"></div></div><div class="why-text">Lorem ipsdolor<br>sit aloremse.</div></div>
<div class="why-item" style="left:286px"><div class="why-ring"><div class="why-icon" role="img" aria-label="Gardener with watering can icon"></div></div><div class="why-text">Lorem ipsdolor<br>sit aloremse.</div></div>
<div class="why-item" style="left:495px"><div class="why-ring"><div class="why-icon" role="img" aria-label="Watering can over sprouts icon"></div></div><div class="why-text">Lorem ipsdolor<br>sit aloremse.</div></div>
<div class="why-item" style="left:702px"><div class="why-ring"><div class="why-icon" role="img" aria-label="Gear with leaves icon"></div></div><div class="why-text">Lorem ipsdolor<br>sit aloremse.</div></div>
<div class="why-item" style="left:909px"><div class="why-ring"><div class="why-icon" role="img" aria-label="Potted plant under sun icon"></div></div><div class="why-text">Lorem ipsdolor<br>sit aloremse.</div></div>

<!-- gallery -->
<h2 class="section-title" style="top:2463px">OUR GALLERY</h2>
<div class="tile" role="img" aria-label="Potted plants and garden tools in sunlight" style="left:126px;top:2544px;width:304px;height:265px;background:
  radial-gradient(ellipse 70px 60px at 140px 150px,#9a9a90,transparent 75%),
  radial-gradient(ellipse 80px 50px at 140px 80px,#b8d24a,transparent 75%),
  radial-gradient(ellipse 50px 50px at 250px 200px,#c0703a,transparent 75%),
  radial-gradient(ellipse 60px 60px at 260px 120px,#f2ecd8,transparent 75%),
  radial-gradient(ellipse 110px 90px at 60px 60px,#d9c860,transparent 75%),
  linear-gradient(135deg,#3b4a1c,#6a7a2a 45%,#7a5a32 80%,#3e2a16)"></div>
<div class="tile" role="img" aria-label="Neatly trimmed hedge beside a green lawn" style="left:448px;top:2544px;width:303px;height:265px;background:
  radial-gradient(ellipse 50px 130px at 250px 130px,#c9ccc6,transparent 75%),
  radial-gradient(ellipse 200px 60px at 130px 230px,#8cc04a,transparent 80%),
  radial-gradient(ellipse 140px 100px at 110px 110px,#3f6e1e,transparent 80%),
  linear-gradient(160deg,#3e6a1c,#5a8a26 55%,#7fb43e)"></div>
<div class="tile" role="img" aria-label="Gravel garden path with stone steps and conifers" style="left:770px;top:2544px;width:302px;height:265px;background:
  radial-gradient(ellipse 130px 70px at 160px 170px,#c4c2bb,transparent 75%),
  radial-gradient(ellipse 70px 20px at 200px 225px,#7a5a3a,transparent 80%),
  radial-gradient(ellipse 60px 40px at 60px 180px,#e6e4dc,transparent 75%),
  radial-gradient(ellipse 100px 60px at 250px 110px,#c8c03a,transparent 75%),
  linear-gradient(180deg,#3f6a2c,#5e8a36 40%,#9fa08e 70%,#8a7a5a)"></div>
<div class="tile" role="img" aria-label="Gardeners planting pink flowers on a lawn" style="left:126px;top:2826px;width:465px;height:266px;background:
  radial-gradient(ellipse 90px 110px at 80px 120px,#8a5a3e,transparent 75%),
  radial-gradient(ellipse 90px 70px at 250px 150px,#d68ac4,transparent 75%),
  radial-gradient(ellipse 60px 50px at 210px 60px,#3cc4a0,transparent 75%),
  radial-gradient(ellipse 70px 60px at 410px 150px,#4ad0b0,transparent 75%),
  radial-gradient(ellipse 70px 60px at 150px 220px,#8aa0b8,transparent 75%),
  linear-gradient(135deg,#2f5a1c,#4e7e2a 50%,#1f3a14)"></div>
<div class="tile" role="img" aria-label="Colourful flower garden in full bloom" style="left:607px;top:2826px;width:465px;height:266px;background:
  radial-gradient(ellipse 70px 50px at 70px 160px,#e03040,transparent 75%),
  radial-gradient(ellipse 60px 50px at 130px 70px,#b050c0,transparent 75%),
  radial-gradient(ellipse 90px 50px at 280px 200px,#e8c050,transparent 75%),
  radial-gradient(ellipse 120px 70px at 330px 60px,#e8e0cc,transparent 75%),
  radial-gradient(ellipse 70px 50px at 410px 200px,#9a7ad0,transparent 75%),
  linear-gradient(160deg,#4a6a28,#7a9a3a 50%,#3e6a24)"></div>
<div class="gold-btn" style="left:502px;top:3141px;width:196px;height:49px">VIEW OUR WORKS</div>

<!-- contact -->
<div class="abs contact-bg" role="img" aria-label="Soft faded view of a landscaped garden"></div>
<svg class="abs" style="left:0;top:3220px" width="1200" height="160" viewBox="0 3220 1200 160">
  <defs>
    <linearGradient id="goldGrad3" x1="0" x2="1"><stop offset="0" stop-color="#b5852a"/><stop offset=".5" stop-color="#f3cf4f"/><stop offset="1" stop-color="#c99a30"/></linearGradient>
  </defs>
  <path d="M0 3220 L1200 3220 L1200 3240 Q600 3380 0 3240 Z" fill="#ffffff"/>
  <path d="M60 3248 Q600 3410 1140 3248 Q600 3366 60 3248 Z" fill="url(#goldGrad3)"/>
</svg>
<h2 class="section-title" style="top:3446px">CONTACT US</h2>
<div class="field" style="left:349px;top:3513px;width:244px;height:46px">Name:</div>
<div class="field" style="left:605px;top:3513px;width:244px;height:46px">Email:</div>
<div class="field" style="left:349px;top:3576px;width:244px;height:45px">Phone:</div>
<div class="field" style="left:605px;top:3576px;width:244px;height:45px">Subject:</div>
<div class="field" style="left:349px;top:3640px;width:500px;height:126px">Message:</div>
<div class="gold-btn" style="left:516px;top:3783px;width:166px;height:47px;font-size:15px;font-weight:700">SUBMIT NOW</div>

<!-- footer -->
<div class="abs footer"></div>
<svg class="abs" style="left:0;top:3860px" width="1200" height="90" viewBox="0 3860 1200 90">
  <defs>
    <linearGradient id="goldGrad4" x1="0" x2="1"><stop offset="0" stop-color="#b5852a"/><stop offset=".5" stop-color="#f3cf4f"/><stop offset="1" stop-color="#c99a30"/></linearGradient>
  </defs>
  <path d="M0 3930 L0 3945 Q600 3850 1200 3945 L1200 3930 Z" fill="#efefed"/>
  <path d="M0 3945 Q600 3850 1200 3945 L1200 3960 L0 3960 Z" fill="#1d1d1d"/>
  <path d="M80 3932 Q600 3858 1120 3932 Q600 3878 80 3932 Z" fill="url(#goldGrad4)"/>
</svg>
<div class="f-head" style="left:202px">MENU</div>
<div class="f-rule" style="left:202px"></div>
<ul class="f-list" style="left:203px"><li>Home</li><li>About us</li><li>Services</li><li>Contact</li><li>Gallery</li></ul>
<div class="f-head" style="left:347px">LINS</div>
<div class="f-rule" style="left:347px"></div>
<ul class="f-list" style="left:348px"><li>Links name 1</li><li>Links name 2</li><li>Links name 3</li><li>Links name 4</li></ul>
<div class="abs f-brand"><div class="brand-name">BRINDMOOR</div><div class="brand-sub">GARDENING</div></div>
<div class="f-head" style="left:810px">CONTACT</div>
<div class="f-rule" style="left:812px"></div>
<div class="f-contact" style="top:4058px">
  <svg width="14" height="18" viewBox="0 0 14 18"><path d="M7 0C3.1 0 0 3 0 6.8 0 11.5 7 18 7 18S14 11.5 14 6.8C14 3 10.9 0 7 0Z" fill="#ffffff"/><circle cx="7" cy="6.8" r="2.4" fill="#1d1d1d"/></svg>
  <span>Lorem Dum street 123 LJD<br>dumy numers 463.</span>
</div>
<div class="f-contact" style="top:4112px">
  <svg width="15" height="15" viewBox="0 0 24 24"><path d="M6.6 10.8c1.4 2.8 3.8 5.1 6.6 6.6l2.2-2.2c.3-.3.7-.4 1-.2 1.1.4 2.3.6 3.6.6.6 0 1 .4 1 1V20c0 .6-.4 1-1 1C10.6 21 3 13.4 3 4c0-.6.4-1 1-1h3.5c.6 0 1 .4 1 1 0 1.2.2 2.4.6 3.6.1.3 0 .7-.2 1L6.6 10.8z" fill="#ffffff"/></svg>
  <span>Phone: 23 555 0190</span>
</div>
<div class="f-contact" style="top:4150px">
  <svg width="15" height="15" viewBox="0 0 24 24" style="margin-top:2px"><path d="M2 5h20v14H2z" fill="#ffffff"/><path d="M2 5l10 8 10-8" fill="none" stroke="#1d1d1d" stroke-width="2"/></svg>
  <span>Email:info@company.com</span>
</div>
<div class="abs f-divider"></div>
<div class="abs copyright">Copyright © 2024&nbsp; All Rights Reserved.</div>

</body>
</html>
```